oloperra Web Design Project

It is a virtual assistance/concierge company that helps the busy professional by remotely providing administrative, technical and/or creative business support services, specializing in the medical device industry. Company name is oloperra.
(website will be oloperra.example)

Allowing things to be done without taking time away from more urgent issues or family/personal time. Partnering with a VA reduces stress, protects cash flow, eliminates administrative hassles, and enables business people to find the success they originally set out to achieve. Saves small businesses and/or individuals on overhead, salary, et. Work is done remotely to offer administrative, clerical, typing and specialist service assistance on a regular, ad-hoc or emergency cover basis.

Though we are capable of addressing the needs of medical professionals and industry representatives due to our experience and knowledge (sales, HCC guidelines, etc.) we do not want to be limited to that market only.

Target Market(s)

Target market would be M/F, 30-50, National, busy, Alpha, entrepreneurs and industry professionals who want/need to do more without sacrifice of life

Industry/Entity Type

Industry

Requirements
Nice to have
• We do have a logo designed via the MakerFolk website that can/should be included. Logo is uploaded.

```html
<!DOCTYPE html>
<html lang="en">
<head>
<meta charset="utf-8">
<title>oloperra</title>
<link rel="stylesheet" href="https://fonts.googleapis.com/css2?family=Source+Sans+3:wght@400;600&display=swap">
<style>
:root{
  --accent:#f05a3c;
  --accent-light:#ff8a6a;
  --navy:#1c3a63;
  --text:#22385a;
  --nav-top:#5b7ea3;
  --nav-bottom:#17375c;
  --page:#f3f3f3;
  --panel:#ffffff;
  --rule:#d9d9d9;
}
*{margin:0;padding:0;box-sizing:border-box}
html,body{width:1200px;height:1049px;overflow:hidden}
body{position:relative;font-family:"Source Sans 3",sans-serif;color:var(--text);
  background:linear-gradient(#dcdcdc 0 10px,#f1f1f1 10px,#fafafa 116px,#fff 145px,#fff 884px,#d6d6d6 884px,#ececec 888px,#f5f5f5 960px,#ececec 1039px,#d4d4d4 1039px)}
.abs{position:absolute}
.brand{left:173px;top:40px;display:flex;align-items:center;gap:10px}
.brand-dot{width:22px;height:22px;border-radius:50%;background:var(--accent)}
.brand-name{font-size:46px;font-weight:600;color:var(--navy);letter-spacing:-1px;line-height:1}
.search{left:779px;top:48px;width:234px;height:28px;background:#fff;border:1px solid #cfcfcf;display:flex;align-items:center;justify-content:space-between;padding:0 8px;font-size:12px;color:#555}
.nav{left:0;top:116px;width:1200px;height:29px;background:linear-gradient(var(--nav-top) 0 30%,#2b4d75 30%,var(--nav-bottom));}
.nav-item{position:absolute;top:0;line-height:29px;font-size:12.5px;color:#fff;transform:translateX(-50%);text-shadow:0 1px 1px #0006}
.nav-sep{position:absolute;top:0;width:1px;height:29px;background:#0d2540;box-shadow:1px 0 0 #6a8bb0}
.hero{left:153px;top:145px;width:893px;height:315px;background:linear-gradient(180deg,#e9eef2,#d7dfe6 60%,#c9d3dc)}
.hero-shadow{left:190px;top:455px;width:820px;height:22px;border-radius:50%;background:radial-gradient(#0005,transparent 70%)}
.dots{left:540px;top:435px;width:111px;height:24px;background:#fff;display:flex;justify-content:center;align-items:center;gap:4px}
.dots span{width:11px;height:11px;border-radius:50%;background:#e2e2e2;border:1px solid #bdbdbd}
.dots span.on{background:var(--accent);border-color:var(--accent)}
.content{left:162px;top:488px;width:876px;height:420px;background:var(--panel);border:1px solid var(--rule)}
.photo{background:linear-gradient(135deg,#e8e4df,#bfb3a6);border:1px solid #aaa}
.h2{font-size:17px;color:var(--accent);font-weight:400}
.para{font-size:11.5px;line-height:19.4px}
.more{font-size:11.5px;color:var(--accent)}
.services{left:174px;top:677px;width:491px;height:194px;background:#fff;border:1px solid var(--rule);border-bottom:4px solid var(--accent);box-shadow:0 2px 4px #0001}
.dotted{border-top:1px dotted #999}
.news{left:716px;top:509px;width:304px;height:290px;background:#fff;box-shadow:8px 0 14px -8px #0003}
.news-item{position:absolute;left:23px;width:258px;font-size:11px;line-height:16.6px}
.news-item p{padding-left:16px;position:relative;text-align:justify}
.news-item p::before{content:"";position:absolute;left:1px;top:5px;border-left:4px solid #999;border-top:3px solid transparent;border-bottom:3px solid transparent}
.news-item .more{display:block;padding-left:18px;margin-top:5px}
.contact{left:719px;top:816px;width:303px;height:90px;background:linear-gradient(90deg,var(--accent),var(--accent-light) 60%,var(--accent));color:#fff}
.copyright{left:0;top:961px;width:1166px;text-align:center;font-size:12px;color:var(--accent)}
</style>
</head>
<body>
<div class="abs brand"><span class="brand-dot"></span><span class="brand-name">oloperra</span></div>
<div class="abs search"><span>Search</span>
<svg width="14" height="16" viewBox="0 0 14 16"><circle cx="5" cy="5" r="3.6" fill="none" stroke="#222" stroke-width="1.8"/><path d="M7.5 8l5 6" stroke="#222" stroke-width="2.4"/></svg></div>

<nav class="abs nav">
  <span class="nav-item" style="left:219px">Home</span>
  <span class="nav-sep" style="left:291px"></span>
  <span class="nav-item" style="left:358px">Medicine &amp; Medical</span>
  <span class="nav-sep" style="left:431px"></span>
  <span class="nav-item" style="left:497px">Health &amp; Beauty</span>
  <span class="nav-sep" style="left:570px"></span>
  <span class="nav-item" style="left:631px">Services</span>
  <span class="nav-sep" style="left:714px"></span>
  <span class="nav-item" style="left:783px">News</span>
  <span class="nav-sep" style="left:873px"></span>
  <span class="nav-item" style="left:951px">Contact Us</span>
</nav>

<div class="abs hero-shadow"></div>
<div class="abs hero" role="img" aria-label="Photo of a smiling team of doctors and nurses in white coats"></div>
<div class="abs dots"><span></span><span></span><span class="on"></span><span></span><span></span><span></span></div>

<div class="abs content"></div>
<div class="abs photo" style="left:173px;top:508px;width:133px;height:126px" role="img" aria-label="Photo of a group of business professionals"></div>
<h2 class="abs h2" style="left:321px;top:510px">Welcome to Our Site</h2>
<p class="abs para" style="left:323px;top:540px;width:344px">Lorem Ipsum is simply dummy text of the printing and typesetting industry. Lorem Ipsum has been the industry's standard dummy text ever since the 1500s, when an unknown printer took a galley of type and scrambled it to make a type specimen book. It has survived not only five centuries, but also the leap into....</p>

<div class="abs services"></div>
<h2 class="abs h2" style="left:190px;top:690px">Services</h2>
<div class="abs dotted" style="left:190px;top:718px;width:447px"></div>
<div class="abs photo" style="left:188px;top:736px;width:169px;height:112px" role="img" aria-label="Photo of a handshake during a client meeting"></div>
<p class="abs para" style="left:371px;top:733px;width:268px;line-height:18.5px;text-align:justify">Lorem Ipsum is simply dummy text of the printing and typesetting industry. Lorem Ipsum has been the industry's standard dummy text ever since the 1500s, when an unknown printer took a galley of type and scrambled it to make a type specimen book.</p>
<a class="abs more" style="left:372px;top:831px">read more+</a>

<section class="abs news">
  <h2 class="h2" style="position:absolute;left:23px;top:24px">News</h2>
  <div class="abs" style="left:23px;top:53px;width:260px;border-top:1px solid #ddd"></div>
  <div class="news-item" style="top:70px"><p>Lorem Ipsum is simply dummy text of the printing and typesetting industry.</p><span class="more">read more+</span></div>
  <div class="abs dotted" style="left:23px;top:132px;width:262px"></div>
  <div class="news-item" style="top:140px"><p>Lorem Ipsum is simply dummy text of the printing and typesetting industry.</p><span class="more">read more+</span></div>
  <div class="abs dotted" style="left:23px;top:203px;width:262px"></div>
  <div class="news-item" style="top:214px"><p>Lorem Ipsum is simply dummy text of the printing and typesetting industry.</p><span class="more">read more+</span></div>
  <div class="abs dotted" style="left:23px;top:277px;width:262px"></div>
</section>
<div class="abs" style="left:716px;top:799px;width:304px;border-top:1px solid var(--accent)"></div>

<address class="abs contact" style="font-style:normal">
  <div class="abs" style="left:24px;top:18px;font-size:11.5px">Street Address, City, Pincode</div>
  <div class="abs" style="left:22px;top:46px;font-size:13px;display:flex;align-items:center;gap:8px">
    <svg width="18" height="14" viewBox="0 0 18 14"><path d="M1 5c0-3 16-3 16 0v2h-4V5H5v2H1z" fill="#fff"/><path d="M4 7h10l2 6H2z" fill="#fff"/><circle cx="9" cy="10" r="1.8" fill="var(--accent)"/></svg>
    <span>: 415.XXX.XXXX</span></div>
  <div class="abs" style="right:10px;top:62px;font-size:13px;display:flex;align-items:center;gap:6px">
    <svg width="19" height="14" viewBox="0 0 19 14"><rect x="0.5" y="0.5" width="18" height="13" fill="none" stroke="#fff"/><path d="M0.5 0.5l9 7 9-7M0.5 13.5l7-6M18.5 13.5l-7-6" fill="none" stroke="#fff"/></svg>
    <span>:info@oloperra.example</span></div>
</address>

<footer class="abs copyright">Copyrights @ 2012 All Rights Reserved</footer>
</body>
</html>
```